B2B EDM Banner Design- Specialist Tech Company

We need a new top-of-email banner for our EDM campaigns for Varnel Brix (www.varnelbrix-example.com
). This banner will sit at the top of every email and must immediately signal the brand, look modern and professional, and be visually aligned with the tech/IT audience.
Size of the banner: Around 728x90 - it must fit at the top of an email blast.
Purpose of the Banner
Establish a strong, recognizable brand identity across all Varnel Brix EDMs
visually consistent with existing banners created for other brands (see reference examples provided)
Communicate Varnel Brix’s value proposition at a glance
Brand Name
Varnel Brix
Tagline (must appear in the banner)
“11,322 whitepapers from 726 companies”
Design Requirements
Style & Tone
Modern, clean, and professional
Tech-centric look and feel
High-quality, sleek, and corporate
Eye-catching but not cluttered
Should feel premium and authoritative
Layout & Composition
Full-width banner for email header
Horizontal orientation similar to the Plomtar and Quindle Staff Archive examples
Include space for the brand name/logo prominently on the left or centered
Integrate the tagline in a readable, secondary position
Optional: a subtle background texture or tech-related abstract pattern (circuitry, network nodes, gradient, etc.)
No busy imagery—should feel clean and trustworthy
Color Palette
Use colors consistent with Varnel Brix branding from www.varnelbrix-example.com
Blues, greys, blacks, and tech-style gradients preferred
Should feel consistent with a B2B IT audience
Typography
Clean, sans-serif fonts (professional/tech-aligned)
Brand name should be bold and prominent
Tagline should be smaller, but still readable on desktop and mobile
Imagery (if used)
Abstract tech shapes, network visuals, geometric patterns, or gradient overlays
Avoid photography of people
Keep imagery subtle so text remains legible
Call-to-Action Button (optional)
None required in this banner (unlike the HR examples)
Banner should remain a pure brand header
Deliverables
Final banner in PNG and JPG formats
2–3 design variations (if possible) for A/B testing
Dimensions optimized for EDM: ~600–700px wide (standard email width), proportionate height

```html
<!DOCTYPE html>
<html lang="en">
<head>
<meta charset="utf-8">
<title>Varnel Brix – EDM Header Variations</title>
<link rel="stylesheet" href="https://fonts.googleapis.com/css2?family=Montserrat:wght@500;600;700&display=swap">
<style>
  :root {
    --page: #ffffff;
    --text: #ffffff;
    --accent: #1ea7ec;
    --navy-1: #0b2a5c;
    --navy-2: #0d1f45;
    --navy-3: #10224b;
    --indigo-1: #1c1f5a;
    --indigo-2: #24226a;
    --royal-1: #0c1a4a;
    --royal-2: #1f4fc4;
    --night-1: #141a3a;
    --cyan-glow: #22b8e6;
    --peach-glow: #f0a08a;
  }
  * { box-sizing: border-box; margin: 0; padding: 0; }
  html, body {
    width: 1171px; height: 1200px; overflow: hidden;
    background: var(--page);
    font-family: "Montserrat", Arial, sans-serif;
  }
  .sheet { position: relative; width: 1171px; height: 1200px; }
  .banner {
    position: absolute; left: 15px; width: 1098px; height: 183px;
    overflow: hidden; color: var(--text);
  }
  .banner--network-light { top: 8px; }
  .banner--network-dark { top: 259px; }
  .banner--dot-wave { top: 509px; }
  .banner--light-burst { top: 760px; }
  .banner--circuit { top: 1010px; height: 190px; }

  .banner__backdrop { position: absolute; inset: 0; }
  .banner--network-light .banner__backdrop {
    background: linear-gradient(100deg, #1a6aa8 0%, var(--navy-1) 45%, var(--navy-2) 100%);
  }
  .banner--network-dark .banner__backdrop {
    background: radial-gradient(ellipse at 8% 80%, #1b4a86 0%, transparent 45%),
                radial-gradient(ellipse at 95% 20%, #1b4a86 0%, transparent 40%),
                var(--navy-3);
  }
  .banner--dot-wave .banner__backdrop {
    background: radial-gradient(ellipse at 5% 90%, #2a5fb0 0%, transparent 45%),
                linear-gradient(90deg, var(--indigo-1), var(--indigo-2));
  }
  .banner--light-burst .banner__backdrop {
    background: radial-gradient(ellipse at 52% 0%, #bfe8ff 0%, #3f8ef0 12%, var(--royal-2) 35%, transparent 70%),
                linear-gradient(90deg, var(--royal-1), #12307e 50%, var(--royal-1));
  }
  .banner--circuit .banner__backdrop {
    background: radial-gradient(ellipse at 0% 30%, var(--cyan-glow) 0%, transparent 35%),
                radial-gradient(ellipse at 100% 30%, var(--cyan-glow) 0%, transparent 30%),
                radial-gradient(ellipse at 100% 100%, var(--peach-glow) 0%, transparent 30%),
                radial-gradient(ellipse at 0% 100%, #c07a8a 0%, transparent 30%),
                linear-gradient(180deg, #1b2244, var(--night-1));
  }

  .brand {
    position: absolute; left: 348px; top: 26px;
    display: flex; align-items: center; gap: 20px;
  }
  .brand__mark {
    width: 92px; height: 92px; border-radius: 50%;
    background: var(--accent); flex: none;
  }
  .brand__name {
    font-weight: 700; font-size: 44px; line-height: 1;
    letter-spacing: -0.5px; text-transform: uppercase;
  }
  .brand__descriptor {
    margin-top: 12px; font-weight: 500; font-size: 19.5px;
    letter-spacing: 1.6px; text-transform: uppercase;
  }
  .tagline {
    position: absolute; left: 0; right: 0; top: 127px;
    text-align: center; font-weight: 500; font-size: 27px;
  }
  .tagline__figure { color: var(--accent); font-weight: 700; }
</style>
</head>
<body>
<main class="sheet">

  <section class="banner banner--network-light">
    <div class="banner__backdrop" role="img" aria-label="Blue gradient with abstract network of connected nodes"></div>
    <div class="brand">
      <span class="brand__mark"></span>
      <div><div class="brand__name">Varnel Brix</div><div class="brand__descriptor">For IT Professionals</div></div>
    </div>
    <p class="tagline"><span class="tagline__figure">11,322</span> whitepapers from <span class="tagline__figure">726</span> companies</p>
  </section>

  <section class="banner banner--network-dark">
    <div class="banner__backdrop" role="img" aria-label="Dark navy background with network node meshes in the corners"></div>
    <div class="brand">
      <span class="brand__mark"></span>
      <div><div class="brand__name">Varnel Brix</div><div class="brand__descriptor">For IT Professionals</div></div>
    </div>
    <p class="tagline"><span class="tagline__figure">11,322</span> whitepapers from <span class="tagline__figure">726</span> companies</p>
  </section>

  <section class="banner banner--dot-wave">
    <div class="banner__backdrop" role="img" aria-label="Indigo background with flowing waves of dotted particles"></div>
    <div class="brand">
      <span class="brand__mark"></span>
      <div><div class="brand__name">Varnel Brix</div><div class="brand__descriptor">For IT Professionals</div></div>
    </div>
    <p class="tagline"><span class="tagline__figure">11,322</span> whitepapers from <span class="tagline__figure">726</span> companies</p>
  </section>

  <section class="banner banner--light-burst">
    <div class="banner__backdrop" role="img" aria-label="Royal blue tech interface with a bright light burst and chevron arrows"></div>
    <div class="brand">
      <span class="brand__mark"></span>
      <div><div class="brand__name">Varnel Brix</div><div class="brand__descriptor">For IT Professionals</div></div>
    </div>
    <p class="tagline"><span class="tagline__figure">11,322</span> whitepapers from <span class="tagline__figure">726</span> companies</p>
  </section>

  <section class="banner banner--circuit">
    <div class="banner__backdrop" role="img" aria-label="Dark background with glowing cyan and peach circuit lines on the sides"></div>
    <div class="brand">
      <span class="brand__mark"></span>
      <div><div class="brand__name">Varnel Brix</div><div class="brand__descriptor">For IT Professionals</div></div>
    </div>
    <p class="tagline"><span class="tagline__figure">11,322</span> whitepapers from <span class="tagline__figure">726</span> companies</p>
  </section>

</main>
</body>
</html>
```